R&T Architects - business card and stationary

Aloha,

We have a simple text logo, we need it incorporated into a business card and also stationary design (letterhead) if possible.

Please check out our website, rtamaui-studio.example for a little more about us. The logo we would like to use is in the upper left corner of the website. It is a simple colored logo based on the Klavica font. We are open to new logo's as well, but we want simple.

Thanks

```html
<!DOCTYPE html>
<html lang="en">
<head>
<meta charset="utf-8">
<title>R&amp;T Architects – Business Card and Letterhead</title>
<link rel="stylesheet" href="https://fonts.googleapis.com/css2?family=Saira+Semi+Condensed:wght@400;600&family=Open+Sans:wght@400;700&display=swap">
<style>
  :root {
    --backdrop: #3c3c3c;
    --brand-green: #8cc63e;
    --brand-brown: #3a2416;
    --paper: #ffffff;
    --ink: #2b2b2b;
    --ink-soft: #6b6b6b;
    --rule: #9a9a9a;
  }
  * { margin: 0; padding: 0; box-sizing: border-box; }
  html, body { width: 1200px; height: 800px; overflow: hidden; }
  body { background: var(--backdrop); font-family: "Open Sans", sans-serif; }
  .board { position: relative; width: 1200px; height: 800px; }
  .piece { position: absolute; }

  .logo {
    font-family: "Saira Semi Condensed", sans-serif;
    font-weight: 600;
    letter-spacing: 0.02em;
    white-space: nowrap;
    line-height: 1;
  }
  .logo--light { color: var(--paper); }
  .logo--dark { color: var(--ink); }
  .web, .card-holder, .card-contact { white-space: nowrap; }

  /* Business card set */
  .card-back-brown { left: 44px; top: 44px; width: 196px; height: 256px; background: var(--brand-brown); }
  .card-front { left: 84px; top: 80px; width: 252px; height: 264px; background: var(--brand-green); overflow: hidden; }
  .card-reverse { left: 356px; top: 80px; width: 256px; height: 264px; background: var(--paper); overflow: hidden; }

  .card-front .logo { position: absolute; left: 96px; top: 104px; font-size: 16px; }
  .card-holder { position: absolute; left: 96px; top: 122px; font-family: "Saira Semi Condensed", sans-serif; font-size: 10px; color: var(--paper); }
  .card-contact { position: absolute; left: 96px; top: 150px; font-family: "Saira Semi Condensed", sans-serif; font-size: 9px; line-height: 1.3; color: var(--paper); }

  .card-reverse .divider { position: absolute; left: 92px; top: 100px; width: 1px; height: 30px; background: var(--rule); }
  .card-reverse .logo { position: absolute; left: 100px; top: 102px; font-size: 16px; }
  .card-reverse .web { position: absolute; left: 100px; top: 120px; font-family: "Saira Semi Condensed", sans-serif; font-size: 8.5px; color: var(--ink); }

  /* Presentation panel */
  .mockup-panel { left: 36px; top: 396px; width: 584px; height: 380px; background: var(--paper); }
  .tilt-card { position: absolute; width: 228px; height: 228px; box-shadow: 2px 3px 8px rgba(0,0,0,0.25); overflow: hidden; }
  .tilt-card--white { left: 320px; top: 20px; background: var(--paper); transform: rotate(13deg); }
  .tilt-card--green { left: 50px; top: 104px; background: var(--brand-green); transform: rotate(-9deg); }
  .tilt-card--white .logo { position: absolute; left: 72px; top: 104px; font-size: 14px; }
  .tilt-card--white .web { position: absolute; left: 72px; top: 120px; font-family: "Saira Semi Condensed", sans-serif; font-size: 7.5px; color: var(--ink); }
  .tilt-card--green .logo { position: absolute; left: 84px; top: 96px; font-size: 14px; }
  .tilt-card--green .card-holder { left: 84px; top: 112px; font-size: 8.5px; }
  .tilt-card--green .card-contact { left: 84px; top: 132px; font-size: 7.5px; }

  /* Folder and letterhead */
  .folder { left: 636px; top: 266px; width: 392px; height: 518px; background: var(--brand-green); }
  .folder .logo { position: absolute; left: 28px; top: 390px; font-size: 22px; }
  .folder .web { position: absolute; left: 28px; top: 416px; font-family: "Saira Semi Condensed", sans-serif; font-size: 10px; color: var(--ink); }

  .letterhead { left: 740px; top: 24px; width: 288px; height: 600px; background: var(--paper); box-shadow: 0 0 6px rgba(0,0,0,0.2); font-size: 5.5px; line-height: 1.65; color: var(--ink-soft); overflow: hidden; }
  .letterhead .logo { position: absolute; left: 18px; top: 20px; font-size: 12px; }
  .letterhead .web { position: absolute; left: 18px; top: 33px; font-family: "Saira Semi Condensed", sans-serif; font-size: 6px; color: var(--ink); }
  .recipient { position: absolute; left: 18px; top: 116px; }
  .subject { position: absolute; left: 18px; top: 176px; font-weight: 700; color: var(--ink); }
  .letter-body { position: absolute; left: 18px; top: 210px; width: 250px; }
  .letter-body p { margin-bottom: 12px; }
  .signer { position: absolute; left: 60px; top: 436px; font-size: 5px; }
  .signature-mark { position: absolute; left: 66px; top: 448px; width: 44px; height: 14px; background: linear-gradient(90deg, #e6e6e6, #cfcfcf); }
  .letter-footer { position: absolute; left: 18px; top: 576px; width: 252px; font-weight: 700; font-size: 5px; color: var(--ink); letter-spacing: 0.06em; white-space: nowrap; }
</style>
</head>
<body>
<main class="board">
  <div class="piece card-back-brown"></div>

  <section class="piece card-front">
    <div class="logo logo--light">R&amp;T Architects</div>
    <div class="card-holder">Daniel Kahale</div>
    <div class="card-contact">48 Palm Lane<br>(808) 555 0142<br>daniel@rtamaui-studio.example</div>
  </section>

  <section class="piece card-reverse">
    <div class="divider"></div>
    <div class="logo logo--dark">R&amp;T Architects</div>
    <div class="web">www.rtamaui-studio.example</div>
  </section>

  <section class="piece mockup-panel">
    <div class="tilt-card tilt-card--white">
      <div class="logo logo--dark">R&amp;T Architects</div>
      <div class="web">www.rtamaui-studio.example</div>
    </div>
    <div class="tilt-card tilt-card--green">
      <div class="logo logo--light">R&amp;T Architects</div>
      <div class="card-holder">Daniel Kahale</div>
      <div class="card-contact">48 Palm Lane<br>(808) 555 0142<br>daniel@rtamaui-studio.example</div>
    </div>
  </section>

  <section class="piece folder">
    <div class="logo logo--light">R&amp;T Architects</div>
    <div class="web">www.rtamaui-studio.example</div>
  </section>

  <article class="piece letterhead">
    <div class="logo logo--dark">R&amp;T Architects</div>
    <div class="web">www.rtamaui-studio.example</div>
    <div class="recipient">To:<br>Leilani Akana<br>22 Harbor Road<br>Kahului, HI</div>
    <div class="subject">Re: proposal for the new coastal residence design</div>
    <div class="letter-body">
      <p>Thank you for meeting with our team last week. We have reviewed the site notes and prepared a first concept for your review, with sketches and a schedule attached.</p>
      <p>Our approach keeps the plan open to the trade winds and the mountain view. Living spaces face the garden, while bedrooms sit quietly to the east. Materials are local stone, timber and lime plaster, chosen for low upkeep in a salty climate. We suggest a second meeting on site to walk the layout and agree the next steps before drawings begin.</p>
      <p>Warm regards from all of us.</p>
    </div>
    <div class="signer">Daniel Kahale, Principal</div>
    <div class="signature-mark" role="img" aria-label="Handwritten signature"></div>
    <div class="letter-footer">R&amp;T Architects · 48 Palm Lane · Lahaina, HI · rtamaui-studio.example</div>
  </article>
</main>
</body>
</html>
```